A new home page for Velmora!

Velmora needs a needs a new home page. Something fresh, engaging and encompassing of the services and features of the velmora product.

The product competitors are trandle.example, fobrisquant.example, brixel metrics

Hi there,

I'm on leave until Wednesday, so I'll look at all the designs and post comments.

Thank you!

Reason: Quantity of submissions and I was on business trip.

Target Market(s)

Anyone with a website that wants to track visitors, use live chat, support, 'hello' like bars, etc.

Industry/Entity Type

Zentaro

Font styles to use
Sans Serif

Colors

Designer to choose colors to be used in the design.

Requirements
Must have
• the home page must showcase somehow the product line, which is
Analytics
SEO
Live Chat
Support Tickets
Heat Maps
Plonkit (like waveshelf)

visit velmora.example for a full feature list.

```html
<!DOCTYPE html>
<html lang="en">
<head>
<meta charset="utf-8">
<title>Velmora – Testimonials and Footer</title>
<link rel="stylesheet" href="https://fonts.googleapis.com/css2?family=Source+Sans+3:wght@400;600;700&display=swap">
<style>
  :root {
    --ink: #111111;
    --paper: #ffffff;
    --quote-grey: #8a8a8a;
    --mark-grey: #c4c4c4;
    --teal: #2bbcc6;
    --dot-idle: #dcdcdc;
    --footer-bg: #202124;
    --footer-rule: #4d4e52;
    --footer-text: #a9aaac;
    --bottom-bg: #000000;
    --white: #ffffff;
  }
  * { margin: 0; padding: 0; box-sizing: border-box; }
  html, body { width: 1200px; height: 707px; overflow: hidden; }
  body {
    position: relative;
    background: var(--paper);
    font-family: "Source Sans 3", sans-serif;
    color: var(--ink);
  }
  .top-rule { position: absolute; top: 0; left: 0; width: 1200px; height: 3px; background: var(--ink); }

  .testimonials { position: absolute; top: 0; left: 0; width: 1200px; height: 347px; }
  .testimonials__title {
    position: absolute; top: 38px; left: 0; width: 1200px;
    text-align: center; font-size: 39px; font-weight: 400; letter-spacing: -0.3px;
  }
  .quote-mark {
    position: absolute; font-family: Georgia, serif; font-weight: 700;
    font-size: 72px; line-height: 1; color: var(--mark-grey);
  }
  .quote-mark--open { left: 264px; top: 90px; }
  .quote-mark--close { left: 888px; top: 146px; }
  .slider-arrow { position: absolute; top: 141px; width: 18px; height: 28px; }
  .slider-arrow--prev { left: 199px; }
  .slider-arrow--next { left: 982px; }
  .testimonial__text {
    position: absolute; top: 120px; left: 290px; width: 620px;
    text-align: center; font-size: 13.8px; line-height: 17.4px; color: var(--quote-grey);
  }
  .testimonial__author {
    position: absolute; top: 243px; left: 0; width: 1212px; text-align: center;
    font-size: 10.6px; line-height: 13.5px;
  }
  .testimonial__role { color: var(--teal); font-weight: 600; }
  .slider-dots { position: absolute; top: 290px; left: 584px; display: flex; gap: 4px; }
  .slider-dots span { width: 8px; height: 8px; border-radius: 50%; background: var(--dot-idle); }
  .slider-dots .is-active { background: var(--teal); }

  .site-footer { position: absolute; top: 347px; left: 0; width: 1200px; height: 280px; background: var(--footer-bg); }
  .footer-col { position: absolute; top: 27px; }
  .footer-col--quick { left: 199px; width: 137px; }
  .footer-col--features { left: 367px; width: 167px; }
  .footer-col--features-more { left: 567px; width: 167px; top: 54px; }
  .footer-col--tools { left: 767px; width: 167px; }
  .footer-col__heading {
    color: var(--white); font-size: 14.5px; font-weight: 700; height: 27px; line-height: 18px;
    border-bottom: 1px solid var(--footer-rule);
  }
  .footer-col__list { list-style: none; }
  .footer-col__list li {
    height: 24px; line-height: 23px; font-size: 10.6px; color: var(--footer-text);
    border-bottom: 1px solid var(--footer-rule);
  }

  .bottom-bar { position: absolute; top: 627px; left: 0; width: 1200px; height: 80px; background: var(--bottom-bg); color: var(--white); }
  .copyright { position: absolute; left: 200px; top: 35px; font-size: 10.6px; }
  .social { position: absolute; left: 636px; top: 33px; display: flex; gap: 5px; }
  .social span { width: 19px; height: 19px; border-radius: 50%; background: var(--white); }
  .bottom-nav { position: absolute; left: 742px; top: 35px; display: flex; align-items: center; font-size: 10.6px; }
  .bottom-nav .sep { width: 3px; height: 3px; background: var(--white); transform: rotate(45deg); margin: 2px 14px 0; }
</style>
</head>
<body>
  <div class="top-rule"></div>

  <section class="testimonials">
    <h2 class="testimonials__title">What our Clients Say?</h2>
    <span class="quote-mark quote-mark--open">“</span>
    <span class="quote-mark quote-mark--close">”</span>
    <svg class="slider-arrow slider-arrow--prev" viewBox="0 0 18 28" aria-label="Previous">
      <polyline points="15,2 4,14 15,26" fill="none" stroke="#d0d0d0" stroke-width="3"/>
    </svg>
    <svg class="slider-arrow slider-arrow--next" viewBox="0 0 18 28" aria-label="Next">
      <polyline points="3,2 14,14 3,26" fill="none" stroke="#d0d0d0" stroke-width="3"/>
    </svg>
    <p class="testimonial__text">
      I noticed how the frequency of hits reported by Velmora closely followed customer phone enquiries,<br>
      peaking at the start of the week. In some cases I could match customers to the detailed paths<br>
      they took through the site, and could see which business areas customers<br>
      were most interested in.
    </p>
    <p class="testimonial__author">
      Maren Tolliver<br>
      <span class="testimonial__role">Product Manager, Web design studio</span>
    </p>
    <div class="slider-dots">
      <span class="is-active"></span><span></span><span></span><span></span>
    </div>
  </section>

  <footer class="site-footer">
    <nav class="footer-col footer-col--quick">
      <h3 class="footer-col__heading">Quick Links</h3>
      <ul class="footer-col__list">
        <li>Home</li><li>Sign Up</li><li>My Account</li><li>Privacy &amp; Security</li>
        <li>About</li><li>Careers</li><li>Contact</li>
      </ul>
    </nav>
    <nav class="footer-col footer-col--features">
      <h3 class="footer-col__heading">Features</h3>
      <ul class="footer-col__list">
        <li>Web Stats</li><li>Traffic Trend Analysis</li><li>Referring Keywords</li>
        <li>Recent Visitor Locations</li><li>Recent Visitor Map</li><li>Actions &amp; Goals</li><li>Heat Maps</li>
      </ul>
    </nav>
    <nav class="footer-col footer-col--features-more">
      <ul class="footer-col__list">
        <li>Inbound Link Monitoring</li><li>Zentaro PageScore Tracking</li><li>Orbisa Rank Tracking</li>
        <li>Keyword Research</li><li>Keyword Position Tracking</li>
      </ul>
    </nav>
    <nav class="footer-col footer-col--tools">
      <h3 class="footer-col__heading">Free Tools</h3>
      <ul class="footer-col__list">
        <li>WebStats Live</li><li>Site Analyzer</li><li>PageScore Badges</li><li>SEO Optimizer</li>
        <li>Web Thumbs</li><li>Bulk Domain Analyzer</li><li>Link &amp; Site Diagnosis</li><li>Tag Clouds</li>
      </ul>
    </nav>
  </footer>

  <div class="bottom-bar">
    <p class="copyright">Copyright 2006 - 2013 © Velmora - All Rights Reserved</p>
    <div class="social" aria-label="Social profiles">
      <span></span><span></span><span></span><span></span>
    </div>
    <nav class="bottom-nav">
      <span>Contact Us</span><span class="sep"></span>
      <span>Terms &amp; Conditions</span><span class="sep"></span>
      <span>Tell a Friend</span>
    </nav>
  </div>
</body>
</html>
```